Computer consultant business card

Plimvo Software is a newly started computer consulting company. It's a small one-man company that provides mostly Android applications but also websites in collaboration with designers. I'm running this company on the side of full time university studies.

I want the final design to be clean and memorable. Be creative! :)

Some inspiration:
http://www.artfenwick.com/design/62242
http://www.artfenwick.com/design/1628455/business-card-design-by-brusqlin
http://www.artfenwick.com/design/918507/business-card-design-by-velinora-quathbridge

See attachment for my company logo.
Updates

I would like to thank everyone for submitting! I'll need a couple of days to review and ultimately select a design.

Target Market(s)

Non-technical entrepreneurs and small companies.

Industry/Entity Type

University

Requirements
Must have
• My company logo.
In any way, both colors from my logo.
First- and last name, e-mail and phone number.
Double-sided design.
Nice to have
• Something creative with the symbol in my logo

```html
<!DOCTYPE html>
<html lang="en">
<head>
<meta charset="utf-8">
<title>Plimvo Software – Business Card</title>
<link rel="stylesheet" href="https://fonts.googleapis.com/css2?family=Arimo:wght@400;700&family=Oswald:wght@600&family=Tinos&display=swap">
<style>
  :root {
    --bg-light: #9a9a9a;
    --bg-dark: #5e5e5e;
    --frame: #2a2a2c;
    --panel: #ecedef;
    --brand-blue: #3560ad;
    --ink: #2c2c2e;
    --ink-soft: #4a4a4c;
    --white: #ffffff;
  }
  * { margin: 0; padding: 0; box-sizing: border-box; }
  html, body { width: 1200px; height: 787px; overflow: hidden; }
  body {
    background: radial-gradient(ellipse at 40% 30%, var(--bg-light), var(--bg-dark) 85%);
    font-family: "Arimo", Arial, sans-serif;
    color: var(--ink);
    position: relative;
  }
  .card {
    position: absolute;
    top: 243px;
    width: 520px;
    height: 300px;
    box-shadow: 0 10px 24px rgba(0,0,0,.35);
  }
  .card--front { left: 55px; }
  .card--back { left: 625px; }
  .card__art { position: absolute; inset: 0; display: block; }
  .card__content { position: absolute; inset: 0; }

  .brand { display: flex; align-items: center; gap: 10px; }
  .brand__dot {
    width: 46px; height: 46px; border-radius: 50%;
    background: var(--brand-blue);
  }
  .brand__name {
    font-family: "Arimo", Arial, sans-serif;
    font-weight: 700;
    font-size: 46px;
    line-height: 1;
    color: var(--ink);
    letter-spacing: -0.5px;
  }

  /* front */
  .front__identity {
    position: absolute; left: 0; right: 0; top: 88px;
    display: flex; flex-direction: column; align-items: center;
  }
  .front__person { margin-top: 6px; margin-left: 60px; text-align: center; font-family: "Tinos", "Times New Roman", serif; color: var(--ink); }
  .front__name { font-size: 21px; line-height: 1.05; }
  .front__position { font-size: 13px; }

  /* back */
  .back__brand { position: absolute; left: 48px; top: 88px; }
  .back__brand .brand__dot { width: 40px; height: 40px; }
  .back__brand .brand__name { font-size: 40px; }
  .back__title {
    position: absolute; left: 108px; top: 134px;
    font-family: "Tinos", "Times New Roman", serif;
    font-size: 18px; line-height: 1.05; letter-spacing: 1px; color: var(--ink);
  }
  .back__person { position: absolute; right: 58px; top: 40px; text-align: left; }
  .back__name { font-family: "Oswald", "Arial Narrow", sans-serif; font-weight: 600; font-size: 17px; color: var(--ink); line-height: 1.1; }
  .back__role { font-size: 8px; color: var(--ink-soft); font-weight: 700; }
  .contact { position: absolute; right: 48px; top: 172px; list-style: none; font-size: 10px; color: var(--ink-soft); }
  .contact__item { display: flex; align-items: center; gap: 8px; height: 15px; }
  .contact__icon { width: 9px; height: 9px; fill: var(--ink); }
</style>
</head>
<body>

<section class="card card--front" aria-label="Business card front">
  <svg class="card__art" viewBox="0 0 520 300" aria-hidden="true">
    <rect width="520" height="300" fill="var(--frame)"/>
    <rect x="26" y="22" width="468" height="256" fill="var(--panel)"/>
    <polygon points="420,0 520,0 520,96" fill="var(--brand-blue)"/>
    <polygon points="408,0 418,0 520,96 520,106" fill="var(--white)"/>
    <polygon points="0,204 0,300 112,300" fill="var(--brand-blue)"/>
    <polygon points="0,194 0,204 112,300 124,300" fill="var(--white)"/>
  </svg>
  <div class="card__content">
    <div class="front__identity">
      <div class="brand">
        <span class="brand__dot"></span>
        <span class="brand__name">plimvo</span>
      </div>
      <div class="front__person">
        <p class="front__name">Your Name</p>
        <p class="front__position">Company Position</p>
      </div>
    </div>
  </div>
</section>

<section class="card card--back" aria-label="Business card back">
  <svg class="card__art" viewBox="0 0 520 300" aria-hidden="true">
    <rect width="520" height="300" fill="var(--frame)"/>
    <rect x="26" y="22" width="468" height="256" fill="var(--panel)"/>
    <polygon points="400,0 520,0 520,80" fill="var(--brand-blue)"/>
    <polygon points="388,0 400,0 520,80 520,90" fill="var(--white)"/>
  </svg>
  <div class="card__content">
    <div class="back__person">
      <p class="back__name">ARLEN VOSS</p>
      <p class="back__role">Graphic Designer</p>
    </div>
    <div class="brand back__brand">
      <span class="brand__dot"></span>
      <span class="brand__name">plimvo</span>
    </div>
    <p class="back__title">MANAGER<br>DIRECTOR</p>
    <ul class="contact">
      <li class="contact__item"><svg class="contact__icon" viewBox="0 0 10 10"><path d="M2 0h2l1 3-1.5 1a6 6 0 0 0 2.5 2.5L7 5l3 1v2a2 2 0 0 1-2 2A8 8 0 0 1 0 2a2 2 0 0 1 2-2z"/></svg>+(000) 1234 5678</li>
      <li class="contact__item"><svg class="contact__icon" viewBox="0 0 10 10"><rect x="0" y="3" width="10" height="7"/><rect x="2" y="0" width="6" height="3"/></svg>+(000) 1234 5679</li>
      <li class="contact__item"><svg class="contact__icon" viewBox="0 0 10 10"><path d="M0 2h10v6H0z M0 2l5 3.5L10 2" stroke="var(--panel)" stroke-width="0.8"/></svg>email@yourdomain.com</li>
      <li class="contact__item"><svg class="contact__icon" viewBox="0 0 10 10"><circle cx="5" cy="5" r="5"/></svg>www.yourwebsite.com</li>
    </ul>
  </div>
</section>

</body>
</html>
```